Web Page for The Brannock Law Firm

The Brannock Law Firm, 7 Quillen Lane, Corvale, Ga 31510 is a one lawyer trial firm specializing in sever personal injury, including auto accidents, trucking accidents, severe injuries from defective products. Mr Brannock also has been successfully trying these, commercial and business disputes, criminal cases and high net worth divorce cases for over 28 years. He has tried over 100 cases to a jury verdict.

Douglas is a member of all the trial courts of the State of Georgia, including the Northern, Middle and Southern District Federal Courts, the Georgia Court of Appeals, The Georgia Supreme Court, the 11th Circuit Federal Court of appeals and the United States Supreme Court. Douglas holds the largest verdict in South Georgia history of $150,000,000.00. He is a Member of the Peachvale Legal Standards Council and an active member of the Meridian Courtroom Advocates Guild.

Douglas R. Brannock graduated from Pinewick Valley High School in Corvale, Georgia in 1978. He received his BBA in Accounting in 1982 and graduated cum laude from the Halloway Institute College of Law in 1986 with a J.D.

Industry/Entity Type

Lawyer

Number of Pages Required

4 page

Requirements
Must have
• Introduction to firm; separate biography of principal; representative cases; testemonials; blog; method of contact

```html
<!DOCTYPE html>
<html lang="en">
<head>
<meta charset="utf-8">
<title>The Vantrell Law Firm</title>
<link href="https://fonts.googleapis.com/css2?family=Arvo:wght@400;700&family=Open+Sans:wght@400;600&display=swap" rel="stylesheet">
<style>
:root{
  --navy:#0b5aa6;
  --deep:#0d5297;
  --mid:#2479cf;
  --sky:#4a9be6;
  --gold:#f2bb18;
  --white:#ffffff;
  --ink:#555b61;
  --grey:#7c8186;
  --pin:#1a86c8;
}
*{margin:0;padding:0;box-sizing:border-box}
html,body{width:1200px;height:927px;overflow:hidden;background:var(--white)}
body{position:relative;font-family:"Open Sans",Arial,sans-serif;color:var(--ink)}
.serif{font-family:"Arvo",Georgia,serif}

.site-header{position:absolute;left:0;top:0;width:1200px;height:112px;background:var(--navy)}
.brand{position:absolute;left:215px;top:11px;width:170px;text-align:center;color:var(--white)}
.brand-dot{width:56px;height:56px;border-radius:50%;background:var(--gold);margin:0 auto 7px}
.brand-name{font-family:"Arvo",Georgia,serif;font-size:13px;line-height:14px;text-transform:uppercase;white-space:nowrap}
.top-contact{position:absolute;right:233px;top:29px;display:flex;align-items:center;gap:16px;color:var(--white);font-size:10px;text-transform:uppercase}
.top-contact span{display:flex;align-items:center;gap:5px}
.social{display:flex;gap:2px}
.social i{display:block;width:12px;height:12px;border-radius:50%;background:var(--white)}
.main-nav{position:absolute;right:233px;top:70px;display:flex;gap:25px;font-size:11.5px;font-weight:600;color:var(--white);text-transform:uppercase}
.main-nav .active{color:var(--gold);border-bottom:2px solid var(--gold);padding-bottom:3px}

.hero{position:absolute;left:233px;top:124px;width:734px;height:125px}
.hero-label{position:absolute;left:0;top:0;width:190px;height:125px;background:var(--gold);color:var(--white);font-size:18px;letter-spacing:.5px;display:flex;align-items:center;justify-content:center}
.hero-label::after{content:"";position:absolute;right:-13px;top:50px;border-left:13px solid var(--gold);border-top:13px solid transparent;border-bottom:13px solid transparent}
.hero-photo{position:absolute;left:190px;top:0;width:544px;height:125px;background:linear-gradient(100deg,#3a3a3a,#9a9a9a 45%,#5a5a5a 70%,#c8c8c8)}

.tile{position:absolute;color:var(--white);text-align:center}
.tile h3{font-family:"Arvo",Georgia,serif;font-weight:400;font-size:11.5px;line-height:15px;text-transform:uppercase;letter-spacing:.3px}
.icon{width:64px;height:64px;border-radius:50%;background:var(--white);margin:24px auto 20px;display:flex;align-items:center;justify-content:center}

.consult{left:233px;top:261px;width:243px;height:322px;background:var(--gold);padding:22px 23px;text-align:left}
.consult h2{font-family:"Arvo",Georgia,serif;font-weight:400;font-size:15px;line-height:21px;text-transform:uppercase;margin-bottom:10px}
.consult h2 b{font-weight:700}
.field{height:27px;background:var(--white);margin-bottom:8px;color:var(--gold);font-size:10.5px;padding:7px 11px;text-transform:uppercase}
.field.msg{height:59px}
.send{height:30px;border:2px solid var(--white);font-family:"Arvo",Georgia,serif;font-size:13px;text-align:center;line-height:26px;text-transform:uppercase}

.auto{left:476px;top:261px;width:245px;height:161px;background:var(--mid)}
.defect{left:721px;top:261px;width:246px;height:161px;background:var(--sky)}
.commercial{left:476px;top:422px;width:245px;height:161px;background:var(--sky)}
.criminal{left:721px;top:422px;width:246px;height:161px;background:var(--deep);text-align:left;padding:17px 20px}
.criminal h3{margin-bottom:6px}
.criminal p{font-size:10px;line-height:14.6px}
.btn{display:inline-block;background:var(--sky);color:var(--white);font-size:9.5px;font-weight:600;padding:5px 10px;text-transform:uppercase;margin-top:11px}
.welcome{left:233px;top:583px;width:488px;height:161px;background:var(--mid);text-align:left;padding:18px 21px}
.welcome h2{font-family:"Arvo",Georgia,serif;font-weight:400;font-size:19px;margin-bottom:9px}
.welcome p{font-size:10px;line-height:14.6px}
.welcome .btn{background:var(--deep);margin-top:12px}
.divorce{left:721px;top:583px;width:246px;height:161px;background:var(--sky)}

.map{position:absolute;left:233px;top:744px;width:387px;height:136px;background:linear-gradient(135deg,#dedede,#f6f6f6 60%,#e8e8e8)}
.contact-label{position:absolute;left:620px;top:744px;width:156px;height:136px;background:var(--gold);color:var(--white);font-size:18px;line-height:24px;text-align:center;display:flex;align-items:center;justify-content:center;text-transform:uppercase}
.contact-label::after{content:"";position:absolute;right:-13px;top:55px;border-left:13px solid var(--gold);border-top:13px solid transparent;border-bottom:13px solid transparent}
.contact-info{position:absolute;left:776px;top:744px;width:191px;height:136px;border:1px solid #e6e6e6;border-left:0;padding:26px 0 0 28px;font-size:10px;color:var(--ink)}
.contact-info li{list-style:none;display:flex;gap:11px;margin-bottom:12px;line-height:14px}
.contact-info .phone{font-size:14px}
.site-footer{position:absolute;left:233px;top:897px;width:734px;font-size:9px;color:var(--grey)}
</style>
</head>
<body>
<header class="site-header">
  <div class="brand">
    <div class="brand-dot"></div>
    <div class="brand-name">The Vantrell Law<br>Firm</div>
  </div>
  <div class="top-contact">
    <span><svg width="14" height="9" viewBox="0 0 14 9"><rect x="0.5" y="0.5" width="13" height="8" fill="none" stroke="#fff"/><path d="M0.5 0.5 7 5 13.5 0.5" fill="none" stroke="#fff"/></svg>INFO@VANTRELLFIRM.COM</span>
    <span><svg width="8" height="11" viewBox="0 0 8 11"><path d="M2 0 0 2c0 4 3 8 6 9l2-2-2-2-1.5 1C3 7 2 5 2 4l1-1z" fill="#fff"/></svg>CALL US : 800 000 0000</span>
    <span class="social"><i></i><i></i><i></i></span>
  </div>
  <nav class="main-nav">
    <span class="active">Home</span><span>About Us</span><span>Services</span><span>Clients</span><span>Press</span><span>Contact Us</span>
  </nav>
</header>

<section class="hero">
  <div class="hero-label serif">WE WE DO</div>
  <div class="hero-photo" role="img" aria-label="Black and white photo of a judge's gavel resting on open law books"></div>
</section>

<form class="tile consult">
  <h2>Request<br><b>Free Consultant</b></h2>
  <div class="field">Name</div>
  <div class="field">Email</div>
  <div class="field">Phone</div>
  <div class="field">Date of Appointment</div>
  <div class="field msg">Message</div>
  <div class="send">Send Request</div>
</form>

<div class="tile auto">
  <div class="icon"><svg width="34" height="24" viewBox="0 0 34 24"><path d="M3 6h18l5 6h6v8H3z" fill="#2479cf"/><circle cx="9" cy="20" r="3.5" fill="#fff" stroke="#2479cf" stroke-width="2"/><circle cx="26" cy="20" r="3.5" fill="#fff" stroke="#2479cf" stroke-width="2"/></svg></div>
  <h3>Auto &amp; Trucking<br>Accidental Case</h3>
</div>
<div class="tile defect">
  <div class="icon"><svg width="34" height="28" viewBox="0 0 34 28"><path d="M30 2h-3l-3 17H6L3 8h22" fill="none" stroke="#4a9be6" stroke-width="2"/><rect x="8" y="10" width="6" height="6" fill="none" stroke="#4a9be6" stroke-width="1.5"/><rect x="15" y="7" width="6" height="9" fill="none" stroke="#4a9be6" stroke-width="1.5"/><circle cx="9" cy="24" r="2.5" fill="#4a9be6"/><circle cx="21" cy="24" r="2.5" fill="#4a9be6"/></svg></div>
  <h3>Severe Injuries from<br>Defective Products</h3>
</div>
<div class="tile commercial">
  <div class="icon"><svg width="34" height="32" viewBox="0 0 34 32"><rect x="4" y="10" width="8" height="20" fill="#4a9be6"/><rect x="12" y="3" width="10" height="27" fill="#4a9be6"/><rect x="22" y="8" width="8" height="22" fill="#4a9be6"/><g fill="#fff"><rect x="14" y="7" width="2" height="3"/><rect x="18" y="7" width="2" height="3"/><rect x="14" y="13" width="2" height="3"/><rect x="18" y="13" width="2" height="3"/><rect x="14" y="19" width="2" height="3"/><rect x="18" y="19" width="2" height="3"/><rect x="6" y="14" width="2" height="3"/><rect x="25" y="12" width="2" height="3"/><rect x="6" y="20" width="2" height="3"/><rect x="25" y="18" width="2" height="3"/></g></svg></div>
  <h3>Commercial and Business<br>Disputes</h3>
</div>
<div class="tile criminal">
  <h3>Criminal Cases</h3>
  <p>Sed quis vehicula neque. Nam maximus justo non sapien eleifend, id pellentesque neque placerat. Maecenas non lobortis leo, quis tempor urna. Praesent efficitur magna diam, eget finibus mi tincidunt ut.</p>
  <span class="btn">Read More</span>
</div>
<div class="tile welcome">
  <h2>Welcome to The Vantrell Law Firm</h2>
  <p>Suspendisse nec tellus dui. Pellentesque ligula lacus, feugiat rutrum pellentesque nec, aliquet in ex. Duis varius nisi eget erat pulvinar, in pretium lacus placerat. Morbi ut justo ac est pharetra consectetur vel ac sapien. Nulla euismod mi non risus ullamcorper, nec aliquam dolor tincidunt. Curabitur in odio venenatis, interdum tellus ut, varius sapien.</p>
  <span class="btn">Read More</span>
</div>
<div class="tile divorce">
  <div class="icon"><svg width="32" height="28" viewBox="0 0 32 28"><path d="M16 27 3 14C-1 9 2 2 8 2c4 0 6 3 8 5 2-2 4-5 8-5 6 0 9 7 5 12z" fill="#4a9be6"/><path d="M17 6l-4 8h5l-3 8" fill="none" stroke="#fff" stroke-width="2"/></svg></div>
  <h3>High Net Worth<br>Divorce Cases</h3>
</div>

<div class="map" role="img" aria-label="Street map showing the firm's office location"></div>
<div class="contact-label serif">Contact<br>Info</div>
<ul class="contact-info">
  <li><svg width="9" height="12" viewBox="0 0 9 12"><path d="M4.5 12C1 7 0 6 0 4.5a4.5 4.5 0 0 1 9 0C9 6 8 7 4.5 12z" fill="#1a86c8"/><circle cx="4.5" cy="4.5" r="1.7" fill="#fff"/></svg><span>Lorem Ipsum, Dollar,Sit,<br>7 Quillen Lane, Corvale</span></li>
  <li><svg width="9" height="12" viewBox="0 0 8 11"><path d="M2 0 0 2c0 4 3 8 6 9l2-2-2-2-1.5 1C3 7 2 5 2 4l1-1z" fill="#1a86c8"/></svg><span class="phone">800 000 0000</span></li>
  <li><svg width="12" height="9" viewBox="0 0 12 9"><rect width="12" height="9" fill="#1a86c8"/><path d="M0 0 6 5 12 0" fill="none" stroke="#fff"/></svg><span>info@vantrellfirm.com</span></li>
</ul>

<footer class="site-footer">© Copyright 2014, The Vantrell Law Firm</footer>
</body>
</html>
```